Tradeshow Banner Design (Qty2, 6'H x 2'W)

Brightwell Contractors is an Electrical, Fire Alarm, and Security Contracting company. For tradeshows, we would like 2 vertical Banners to put behind our booth. Our colors are Red, Grey & Black. I would like the Banners to be informative on what services we provide, with some appealing Graphic Design. (bwc-kmo.com)
Slogan: Safeguarding Communities Electrical, Fire & Security Solutions
Target Market(s)
Commercial Construction Clients
Industry/Entity Type
Electrical / Construction
Font styles to use
Other font styles liked:
- Aileron
Colors
EB3D1F
EC4F4E
F09395
F8D3D4
FCEDEE
Requirements
Must have
- Our Logo, Color Scheme, Brief Caption of the services we provide
Nice to have
- Appealing Imagery & a modern/simplistic design

```html
<!DOCTYPE html>
<html lang="en">
<head>
<meta charset="utf-8">
<title>Brightwell Contractors – Tradeshow Banner</title>
<link rel="stylesheet" href="https://fonts.googleapis.com/css2?family=Bebas+Neue&family=Arimo:wght@400;500&display=swap">
<style>
  :root {
    --red-deep: #a82a26;
    --red-main: #d23a33;
    --red-bright: #e8423b;
    --red-dark: #5a1513;
    --night: #1a0807;
    --white: #ffffff;
    --rule: rgba(255, 255, 255, 0.35);
  }
  html, body {
    margin: 0;
    padding: 0;
    width: 1200px;
    height: 3673px;
    overflow: hidden;
    background: var(--night);
  }
  .banner {
    position: relative;
    width: 1200px;
    height: 3673px;
    overflow: hidden;
    background: linear-gradient(180deg, var(--red-deep) 0%, var(--red-main) 22%, var(--red-bright) 45%, var(--red-main) 55%);
    color: var(--white);
    font-family: "Arimo", Arial, sans-serif;
  }
  .backdrop-flame {
    position: absolute;
    left: 0;
    top: 400px;
    width: 1200px;
    height: 1700px;
    background: radial-gradient(ellipse 45% 55% at 60% 55%, rgba(255, 90, 80, 0.35), rgba(255, 90, 80, 0) 70%);
  }
  .scene-photo {
    position: absolute;
    left: 0;
    top: 1880px;
    width: 1200px;
    height: 1793px;
    background: linear-gradient(180deg, rgba(210, 58, 51, 0) 0%, #b7342e 18%, #8c2522 40%, #5a1513 62%, #2e0c0b 82%, var(--night) 100%);
  }
  .brand {
    position: absolute;
    top: 230px;
    left: 0;
    width: 1200px;
    display: flex;
    justify-content: center;
    align-items: center;
    gap: 34px;
  }
  .brand-mark {
    width: 150px;
    height: 150px;
    border-radius: 50%;
    background: var(--white);
  }
  .brand-name {
    font-family: "Bebas Neue", Impact, sans-serif;
    font-size: 92px;
    line-height: 0.92;
    color: var(--white);
  }
  .headline {
    position: absolute;
    top: 690px;
    left: 0;
    width: 1200px;
    margin: 0;
    text-align: center;
    font-family: "Bebas Neue", Impact, sans-serif;
    font-weight: 400;
    line-height: 0.86;
  }
  .headline span { display: block; }
  .headline .line-safe { font-size: 455px; letter-spacing: 4px; }
  .headline .line-guarding { font-size: 240px; margin-top: 10px; letter-spacing: -1px; }
  .headline .line-communities { font-size: 214px; margin-top: 8px; letter-spacing: -1px; }
  .tagline {
    position: absolute;
    top: 1490px;
    left: 0;
    width: 1226px;
    margin: 0;
    text-align: center;
    font-size: 62px;
    line-height: 1.2;
  }
  .services-rule-v {
    position: absolute;
    left: 630px;
    top: 1795px;
    width: 3px;
    height: 720px;
    background: var(--rule);
  }
  .services-rule-h {
    position: absolute;
    left: 210px;
    top: 2163px;
    width: 838px;
    height: 3px;
    background: var(--rule);
  }
  .service {
    position: absolute;
    width: 420px;
    text-align: center;
    font-size: 52px;
    line-height: 1.25;
  }
  .service svg { display: block; margin: 0 auto 18px; fill: var(--white); }
  .service-fire { left: 183px; top: 1765px; }
  .service-electrical { left: 652px; top: 1765px; }
  .service-surveillance { left: 217px; top: 2195px; }
  .service-security { left: 650px; top: 2195px; }
  .certifications {
    position: absolute;
    top: 3130px;
    left: 0;
    width: 1200px;
    display: flex;
    justify-content: center;
    gap: 150px;
    align-items: center;
  }
  .cert-badge-round {
    width: 135px;
    height: 135px;
    border-radius: 50%;
    background: var(--white);
  }
  .cert-badge-square {
    width: 135px;
    height: 135px;
    border-radius: 18px;
    background: var(--white);
  }
</style>
</head>
<body>
<main class="banner">
  <div class="backdrop-flame" role="img" aria-label="Large soft flame shape glowing behind the headline"></div>
  <div class="scene-photo" role="img" aria-label="Photo of a modern apartment building at dusk with lit landscaping, tinted red"></div>

  <header class="brand">
    <div class="brand-mark"></div>
    <div class="brand-name">BRIGHTWELL<br>CONTRACTORS</div>
  </header>

  <h1 class="headline">
    <span class="line-safe">SAFE</span>
    <span class="line-guarding">GUARDING</span>
    <span class="line-communities">COMMUNITIES.</span>
  </h1>

  <p class="tagline">We help our client<br>get peace of mind</p>

  <div class="services-rule-v"></div>
  <div class="services-rule-h"></div>

  <div class="service service-fire">
    <svg width="150" height="170" viewBox="0 0 60 68" aria-hidden="true">
      <path d="M30 2 C34 14 48 22 48 42 C48 56 40 66 30 66 C20 66 12 56 12 42 C12 32 18 26 22 20 C22 28 25 32 28 34 C26 22 28 12 30 2 Z M30 40 C27 46 22 49 22 56 C22 61 26 64 30 64 C34 64 38 61 38 56 C38 49 33 46 30 40 Z"/>
    </svg>
    Fire<br>Protection
  </div>

  <div class="service service-electrical">
    <svg width="130" height="170" viewBox="0 0 50 68" aria-hidden="true">
      <path d="M34 2 L6 38 L22 38 L14 66 L44 26 L28 26 Z"/>
    </svg>
    Electrical<br>Services
  </div>

  <div class="service service-surveillance">
    <svg width="220" height="170" viewBox="0 0 88 68" aria-hidden="true">
      <path d="M14 10 L80 26 L74 46 L10 30 Z"/>
      <path d="M36 34 L50 38 L46 48 L32 44 Z"/>
      <path d="M2 36 L8 36 L8 46 L30 46 L30 52 L8 52 L8 64 L2 64 Z"/>
      <rect x="22" y="40" width="14" height="6" transform="rotate(-30 29 43)"/>
    </svg>
    Surveillance
  </div>

  <div class="service service-security">
    <svg width="160" height="170" viewBox="0 0 60 68" aria-hidden="true">
      <path d="M30 2 L56 12 C56 40 46 58 30 66 C14 58 4 40 4 12 Z" fill="none" stroke="#ffffff" stroke-width="5" stroke-linejoin="round"/>
      <path d="M18 34 L27 43 L43 25" fill="none" stroke="#ffffff" stroke-width="5" stroke-linecap="round" stroke-linejoin="round"/>
    </svg>
    Security
  </div>

  <footer class="certifications">
    <div class="cert-badge-round"></div>
    <div class="cert-badge-square"></div>
  </footer>
</main>
</body>
</html>
```